Plakat-Design für Vereinsfest
Zielgruppe
Unser Verein veranstaltet jedes Jahr im August das Vereinsfest 'Sonnwendtag', das in einem kleinen Wäldchen innerhalb des Heimatortes stattfindet. Am Samstag und Sonntag sorgen verschiedene Musikgruppen für Unterhaltung. Es soll ein Veranstaltungsplakat gestaltet werden, dass sich an die Vorgaben (siehe unten) hält und die Veranstaltung bewirbt.
Zielgruppe sind Bürger des Heimatortes.
Aufgabenstellung
Das Vereinslogo ist beigefügt und sollte prominent auf dem Plakat vertreten sein, Logo und Schriftzug können auch getrennt oder anders angeordnet werden. Der Veranstaltungstitel lautet "Sonnwendtag", es findet am 20. und 21. August "Am Hirtenstein" (Veranstaltungsort) statt.
Programmpunkte: Samstag: Musikalische Unterhaltung mit den Bachpfeifern; Sonntag: Musikalische Unterhaltung mit den Moorbachrabauken
Uhrzeiten sollten enthalten sein:
Beginn Samstag: ab 15 Uhr
Beginn Sonntag: ab 10 Uhr
Das Plakat soll gut leserlich auch aus der Entfernung sein, da es an Straßen plakatiert wird.
Das Plakat soll für spätere Jahre editierbar sein.
Schriftart im Logo: Californian FB Bold (muss aber nicht auf andere Textelemente angewendet werden). Das Plakat soll in DIN A2 gedruckt werden. Die Webadresse sollte auf dem Plakat stehen.

```html
<!DOCTYPE html>
<html lang="de">
<head>
<meta charset="utf-8">
<title>Sonnwendtag – Plakat</title>
<link rel="stylesheet" href="https://fonts.googleapis.com/css2?family=Cinzel:wght@600;700&family=Libre+Baskerville:wght@700&family=Crimson+Text:wght@600;700&display=swap">
<style>
  :root {
    --stage: #e6e4e0;
    --paper-top: #f3f6fb;
    --paper-bottom: #c9d9f0;
    --blue-deep: #0a4f86;
    --blue-mid: #0d6fb0;
    --blue-dark: #173f63;
    --ink-blue: #16598c;
    --ink-grey: #4a4540;
    --box-grey: #3d3d3d;
    --white: #ffffff;
  }
  * { box-sizing: border-box; margin: 0; padding: 0; }
  html, body { width: 1157px; height: 1200px; overflow: hidden; }
  body { background: var(--stage); position: relative; }

  .poster {
    position: absolute; left: 175px; top: 30px;
    width: 806px; height: 1140px;
    background: linear-gradient(180deg, var(--paper-top) 35%, var(--paper-bottom) 100%);
    overflow: hidden;
    box-shadow: 0 6px 24px rgba(0,0,0,.18);
  }
  .frame {
    position: absolute; left: 28px; right: 28px; top: 280px; bottom: 28px;
    border: 3px solid var(--ink-blue);
    outline: 1.5px solid var(--ink-blue); outline-offset: -9px;
  }
  .header { position: absolute; left: 0; top: 0; width: 806px; height: 470px; }
  .header svg { display: block; }
  .musicians {
    position: absolute; left: 210px; top: 80px; width: 400px; height: 150px;
    background: linear-gradient(180deg, rgba(255,255,255,.85), rgba(255,255,255,.6));
    border-radius: 40px 40px 6px 6px;
  }
  .notes-left, .notes-right {
    position: absolute; top: 12px; width: 190px; height: 170px;
    background: rgba(255,255,255,.22); border-radius: 50%;
  }
  .notes-left { left: 14px; }
  .notes-right { right: 14px; }
  .title {
    position: absolute; left: 0; right: 0; top: 245px;
    text-align: center; color: var(--white);
    font: 700 90px/1 "Cinzel", serif; letter-spacing: 1px;
    font-variant: small-caps;
  }
  .title .big { font-size: 108px; }

  .details { position: absolute; left: 0; right: 0; top: 505px; text-align: center; }
  .date {
    color: var(--ink-blue);
    font: 700 70px/1 "Cinzel", serif;
  }
  .venue {
    margin-top: 10px; color: var(--ink-blue);
    font: 700 48px/1 "Cinzel", serif;
  }
  .program { margin-top: 28px; }
  .day {
    color: var(--ink-grey);
    font: 700 30px/1.1 "Libre Baskerville", serif;
  }
  .act {
    color: var(--ink-blue);
    font: 700 27px/1.2 "Crimson Text", serif;
    margin-bottom: 6px;
  }
  .times {
    display: inline-block; margin-top: 30px;
    background: var(--box-grey); color: var(--white);
    padding: 14px 30px;
    font: 700 29px/1.25 "Crimson Text", serif;
    text-align: left;
  }
  .corner {
    position: absolute; bottom: 46px; width: 170px; height: 150px;
    background: rgba(22,89,140,.10);
  }
  .corner-left { left: 46px; border-radius: 0 80% 0 0; }
  .corner-right { right: 46px; border-radius: 80% 0 0 0; }

  .club {
    position: absolute; left: 0; right: 0; top: 970px;
    display: flex; justify-content: center; align-items: center; gap: 18px;
  }
  .club-mark {
    width: 96px; height: 96px; border-radius: 50%;
    background: #7f98cc; flex: none;
  }
  .club-name {
    color: #1f2f6b;
    font: 700 26px/1.15 "Crimson Text", serif;
  }
</style>
</head>
<body>
  <main class="poster">
    <div class="frame"></div>

    <header class="header">
      <svg width="806" height="470" viewBox="0 0 806 470" aria-hidden="true">
        <defs>
          <linearGradient id="curtain" x1="0" y1="0" x2="1" y2="1">
            <stop offset="0" stop-color="#0a4a82"/>
            <stop offset="0.5" stop-color="#0d74b6"/>
            <stop offset="1" stop-color="#084478"/>
          </linearGradient>
        </defs>
        <path fill="#1b4a70" d="M0,0 H806 V330 C806,390 770,410 710,408 C668,406 648,398 626,414 C594,458 500,470 403,470 C306,470 212,458 180,414 C158,398 138,406 96,408 C36,410 0,390 0,330 Z"/>
        <path fill="url(#curtain)" d="M0,0 H806 V300 C806,360 765,382 705,380 C662,379 642,370 620,386 C590,430 500,446 403,446 C306,446 216,430 186,386 C164,370 144,379 101,380 C41,382 0,360 0,300 Z"/>
      </svg>
      <div class="notes-left" role="img" aria-label="Notenlinien mit Violinschlüssel und Noten"></div>
      <div class="notes-right" role="img" aria-label="Geschwungene Notenlinien mit Noten"></div>
      <div class="musicians" role="img" aria-label="Weiße Silhouetten einer Blaskapelle mit Saxofon, Trompeten und Tuba"></div>
      <h1 class="title"><span class="big">S</span>onnwendtag</h1>
    </header>

    <section class="details">
      <p class="date">20 - 21 AUGUST</p>
      <p class="venue">“Am Hirtenstein”</p>
      <div class="program">
        <p class="day">SAMSTAG:</p>
        <p class="act">Musikalische Unterhaltung mit den Bachpfeifern</p>
        <p class="day">SONNTAG:</p>
        <p class="act">Musikalische Unterhaltung mit den<br>Moorbachrabauken</p>
      </div>
      <div class="times">
        Beginn Samstag: ab 15 Uhr<br>
        Beginn Sonntag: ab 10 Uhr
      </div>
    </section>

    <div class="corner corner-left" role="img" aria-label="Rankenornament in der Ecke"></div>
    <div class="corner corner-right" role="img" aria-label="Rankenornament in der Ecke"></div>

    <footer class="club">
      <span class="club-mark"></span>
      <p class="club-name">Historischer Heimat- und<br>Trachtenverein<br>Lindenau e.V.</p>
    </footer>
  </main>
</body>
</html>
```